Haskell and Dunmore Ranch Insurance

Would like you all to design a logo for our Business cards and possible letterhead.
This business provides Ranch insurance for folks in Texas, New Mexico, and Oklahoma

Ggood stuff everybody, be sure to include email and Mobil for both of us on all designs

Thanks

Hello All

Wanted to let you all know i am going to extend deadline a few days, and add some more $$ to the budget

Reason: Give everybody a bit ,more time, and I added more money

Appreciate all of yalls hard work, will review and provide feed back hopefully today, been a little whacky with the holidays and all

```html
<!DOCTYPE html>
<html lang="en">
<head>
<meta charset="utf-8">
<title>Haskell and Dunmore – Letterhead</title>
<link rel="stylesheet" href="https://fonts.googleapis.com/css2?family=Arimo:wght@400&family=Roboto+Condensed:wght@500&display=swap">
<style>
  :root {
    --brown: #7d4b35;
    --stone: #6e625e;
    --paper: #ffffff;
    --frame: #b9b9b9;
    --ghost: #f1f1f1;
  }
  * { margin: 0; padding: 0; box-sizing: border-box; }
  html, body { width: 848px; height: 1200px; overflow: hidden; background: var(--paper); }
  .letterhead {
    position: relative;
    width: 848px;
    height: 1200px;
    background: var(--paper);
    border: 1px solid var(--frame);
    overflow: hidden;
    font-family: "Arimo", Arial, sans-serif;
  }
  .brand-dot {
    position: absolute;
    left: 41px;
    top: 17px;
    width: 74px;
    height: 74px;
    border-radius: 50%;
    background: var(--stone);
  }
  .brand-name {
    position: absolute;
    left: 125px;
    top: 62px;
    font-size: 30px;
    line-height: 30px;
    color: var(--brown);
    white-space: nowrap;
  }
  .contact {
    position: absolute;
    left: 614px;
    top: 18px;
    font-family: "Roboto Condensed", "Arial Narrow", sans-serif;
    font-weight: 500;
    font-size: 15.5px;
    line-height: 21px;
    color: var(--brown);
    letter-spacing: -0.2px;
  }
  .contact .indent { padding-left: 92px; }
  .rule {
    position: absolute;
    left: 0;
    width: 100%;
    background: var(--brown);
  }
  .rule-top-1 { top: 119px; height: 2px; }
  .rule-top-2 { top: 124px; height: 2px; }
  .rule-foot { top: 1136px; height: 2px; }
  .ghost-name {
    position: absolute;
    left: 438px;
    top: 636px;
    transform: translate(-50%, -50%) rotate(-52deg);
    font-size: 80px;
    color: var(--ghost);
    white-space: nowrap;
  }
  .owners {
    position: absolute;
    left: 40px;
    right: 40px;
    top: 1104px;
    display: flex;
    justify-content: space-between;
    font-family: "Roboto Condensed", "Arial Narrow", sans-serif;
    font-weight: 500;
    font-size: 14px;
    line-height: 20px;
    color: var(--brown);
    white-space: nowrap;
  }
  .footer-band {
    position: absolute;
    left: 0;
    top: 1142px;
    width: 100%;
    height: 58px;
    background: var(--brown);
    color: #fff;
    font-size: 26px;
    letter-spacing: 0.5px;
    display: flex;
    align-items: center;
    justify-content: center;
  }
</style>
</head>
<body>
  <div class="letterhead">
    <div class="ghost-name" aria-hidden="true">Haskell and Dunmore</div>

    <div class="brand-dot"></div>
    <div class="brand-name">Haskell and Dunmore</div>

    <div class="contact">
      <div>Address : 408 W Oak St. Ozona,</div>
      <div class="indent">TX 76943</div>
      <div>www.haskellanddunmore.com</div>
      <div>Phone : 325-555-0148</div>
    </div>

    <div class="rule rule-top-1"></div>
    <div class="rule rule-top-2"></div>

    <div class="owners">
      <div class="owner">Wade Haskell · Mobile : 325-555-0162 · wade@haskellanddunmore.com</div>
      <div class="owner">Clay Dunmore · Mobile : 325-555-0177 · clay@haskellanddunmore.com</div>
    </div>

    <div class="rule rule-foot"></div>
    <div class="footer-band">Address : 408 W Oak St. Ozona, TX 76943</div>
  </div>
</body>
</html>
```